VORLANE (PTY)LTD Website design

WEBSITE design based on our different divisions in our organization.
Our company specializes in the following.
Construction
Property development
Demolition
Mining
Transport
Manufacturing of concrete bricks and blocks
Lightweight concrete Readymix
I want a very modern website and look that fits in with our organization and the changing times of the world.
The website must be very professional and crisp and should appeal to both the younger generation and older generation of business leaders and.
The website must be very user friendly and easy to navigate, simple yet modern, professional and corporate.

```html
<!DOCTYPE html>
<html lang="en">
<head>
<meta charset="UTF-8">
<title>VORLANE (PTY)LTD – Moving Mountains</title>
<link href="https://fonts.googleapis.com/css2?family=Montserrat:wght@400;500;600;800&display=swap" rel="stylesheet">
<style>
  :root {
    --sky-deep: #04111d;
    --sky-mid: #0b3550;
    --glass-blue: #1d4a66;
    --glass-gold: #b8932f;
    --glow-gold: #e9c35a;
    --ink-white: #ffffff;
    --band-shade: rgba(20, 28, 18, 0.72);
    --accent-violet: #4a1fd6;
  }
  * { margin: 0; padding: 0; box-sizing: border-box; }
  html, body {
    width: 1200px;
    height: 932px;
    overflow: hidden;
    background: var(--sky-deep);
    font-family: "Montserrat", Arial, sans-serif;
    color: var(--ink-white);
  }
  .hero {
    position: relative;
    width: 1200px;
    height: 932px;
    overflow: hidden;
  }
  .hero-backdrop {
    position: absolute;
    inset: 0;
    background:
      radial-gradient(ellipse 60% 70% at 78% 52%, var(--glow-gold) 0%, rgba(184,147,47,0.55) 40%, rgba(184,147,47,0) 75%),
      radial-gradient(ellipse 40% 60% at 40% 55%, rgba(29,74,102,0.9) 0%, rgba(29,74,102,0) 80%),
      linear-gradient(135deg, var(--sky-mid) 0%, var(--sky-deep) 45%, #2a2410 80%, #120f06 100%);
  }
  .site-header {
    position: absolute;
    top: 0; left: 0; right: 0;
    height: 130px;
    display: flex;
    justify-content: space-between;
    align-items: flex-start;
    padding: 40px 32px 0 52px;
  }
  .brand {
    display: flex;
    align-items: center;
    gap: 12px;
    font-size: 44px;
    font-weight: 600;
    letter-spacing: 1px;
    line-height: 1;
    margin-top: 8px;
  }
  .brand-square {
    width: 22px;
    height: 22px;
    background: var(--ink-white);
  }
  .main-nav {
    display: flex;
    gap: 34px;
    margin-top: 8px;
  }
  .main-nav a {
    color: var(--ink-white);
    text-decoration: none;
    font-size: 19px;
    font-weight: 500;
    letter-spacing: 0.3px;
  }
  .headline {
    position: absolute;
    left: 0; right: 0;
    top: 452px;
    text-align: center;
    font-weight: 800;
    font-size: 114px;
    line-height: 112px;
    letter-spacing: 1px;
    text-shadow: 4px 5px 8px rgba(0,0,0,0.55);
  }
  .division-band {
    position: absolute;
    left: 0; right: 0;
    top: 712px;
    height: 50px;
    background: var(--band-shade);
    display: flex;
    justify-content: center;
    align-items: center;
    gap: 30px;
    font-size: 21px;
    font-weight: 500;
    letter-spacing: 0.2px;
  }
  .cta-button {
    position: absolute;
    left: 428px;
    top: 786px;
    width: 345px;
    height: 79px;
    background: var(--accent-violet);
    color: var(--ink-white);
    text-decoration: none;
    display: flex;
    align-items: center;
    justify-content: center;
    font-size: 28px;
    font-weight: 400;
    letter-spacing: 2px;
  }
</style>
</head>
<body>
  <main class="hero">
    <div class="hero-backdrop" role="img" aria-label="Night photograph looking up at a glass office building with warmly lit golden windows under a starry blue sky"></div>

    <header class="site-header">
      <div class="brand"><span class="brand-square"></span>VORLANE</div>
      <nav class="main-nav">
        <a href="#">HOME</a>
        <a href="#">ABOUT</a>
        <a href="#">SERVICES</a>
        <a href="#">CONTACT</a>
      </nav>
    </header>

    <h1 class="headline">MOVING<br>MOUNTAINS</h1>

    <div class="division-band">
      <span>CONSTRUCTION</span>
      <span>PROPERTY DEVELOPMENT</span>
      <span>DEMOLITION</span>
      <span>MINING</span>
      <span>TRANSPORT</span>
    </div>

    <a class="cta-button" href="#">LEARN MORE</a>
  </main>
</body>
</html>
```